Cafe menu flyer design

I need if possible A4 double sided menus. Two exemplars: first will contain breakfast menu on one side & refreshments menu on the other side, second exemplar will contain lunch menu on one side & refreshments menu on the other side. We do not need a description of the cafe or any history on these flyers, but design should reflect our surroundings and activities this area. We are located in main ski resort in UK-Cairngorm Mountains, right on the main ski road. The slopes are only 2 miles away from us. We are also very popular with wild life enthusiasts. Continues in design brief!

Cafe

```html
<!DOCTYPE html>
<html lang="en">
<head>
<meta charset="utf-8">
<title>Elspeth's @ Lochan Cafe – Lunch Menu</title>
<link rel="stylesheet" href="https://fonts.googleapis.com/css2?family=Open+Sans:ital,wght@0,400;0,600;0,700;1,600;1,700&family=Tinos:ital,wght@1,700&display=swap">
<style>
  :root {
    --backdrop: #8fa3a4;
    --flyer-orange: #ec9b1f;
    --ink-blue: #2b3192;
    --ink-dark: #2e2c47;
    --price-blue: #3b3f7e;
    --badge-plum: #9a4469;
    --squirrel-rust: #d8661c;
    --squirrel-cream: #f2d6b0;
  }
  * { box-sizing: border-box; margin: 0; padding: 0; }
  html, body { width: 1200px; height: 960px; overflow: hidden; }
  body {
    background: var(--backdrop);
    font-family: "Open Sans", Arial, sans-serif;
    color: var(--ink-dark);
  }
  .flyer {
    position: absolute;
    left: 275px; top: 20px;
    width: 650px; height: 920px;
    background: var(--flyer-orange);
    overflow: hidden;
  }
  .cafe-title {
    position: absolute;
    top: 52px; left: 0; width: 650px;
    text-align: center;
    font-weight: 700;
    font-size: 30px;
    color: var(--ink-blue);
    letter-spacing: -0.2px;
  }
  .badge {
    position: absolute;
    left: 502px; top: 6px;
    width: 128px; height: 128px;
  }
  .section-heading {
    font-weight: 700;
    font-size: 17px;
    color: var(--ink-blue);
    padding-bottom: 4px;
    border-bottom: 2px solid var(--ink-blue);
    margin-bottom: 22px;
  }
  .column { position: absolute; top: 112px; }
  .column--lunch { left: 11px; width: 305px; z-index: 1; }
  .column--drinks { left: 333px; width: 299px; }
  .column-divider {
    position: absolute;
    left: 323px; top: 114px;
    width: 2px; height: 738px;
    background: var(--ink-blue);
  }
  .menu-list { list-style: none; font-size: 11px; line-height: 16px; }
  .menu-item {
    display: flex;
    justify-content: space-between;
    align-items: flex-end;
    gap: 8px;
    margin-bottom: 9px;
  }
  .column--drinks .menu-item { margin-bottom: 9.8px; }
  .menu-item .price { color: var(--price-blue); white-space: nowrap; }
  .menu-item--stack { display: block; }
  .menu-item .inline-price { color: var(--price-blue); }
  .menu-item .aside { font-style: italic; font-weight: 600; }
  .note {
    font-style: italic;
    font-weight: 700;
    font-size: 11px;
    line-height: 15px;
    color: var(--ink-blue);
  }
  .column--lunch .note--first { margin-top: 2px; }
  .column--lunch .note--ask { margin-top: 10px; }
  .column--drinks .note--first { margin-top: 0; }
  .column--drinks .note--season { margin-top: 6px; }
  .wildlife-strip {
    position: absolute;
    left: 0; top: 752px;
    width: 300px; height: 100px;
    background: linear-gradient(90deg, var(--squirrel-rust) 0%, var(--squirrel-cream) 35%, var(--squirrel-rust) 55%, var(--squirrel-cream) 75%, var(--squirrel-rust) 100%);
    opacity: 0.55;
  }
  .footer-rule {
    position: absolute;
    left: 0; top: 852px;
    width: 650px; height: 2px;
    background: var(--ink-blue);
  }
  .footer {
    position: absolute;
    left: 0; top: 860px; width: 650px;
    text-align: center;
    font-family: "Tinos", "Times New Roman", serif;
    font-style: italic;
    font-weight: 700;
    font-size: 12.5px;
    line-height: 17px;
    color: var(--ink-blue);
  }
</style>
</head>
<body>
  <main class="flyer">
    <h1 class="cafe-title">Elspeth’s @ Lochan Cafe</h1>

    <svg class="badge" viewBox="0 0 128 128" aria-hidden="true">
      <circle cx="64" cy="64" r="62" fill="var(--badge-plum)"/>
    </svg>

    <div class="wildlife-strip" role="img" aria-label="Illustration of a row of red squirrels"></div>

    <section class="column column--lunch">
      <h2 class="section-heading">Lunch menu 12-4pm</h2>
      <ul class="menu-list">
        <li class="menu-item"><span>Soup of the day, served with brown roll &amp; butter</span><span class="price">£3.75</span></li>
        <li class="menu-item menu-item--stack">Freshly made toasties:&nbsp; one filling <span class="inline-price">£3.20</span>, two fillings <span class="inline-price">£4.20</span></li>
        <li class="menu-item">Sundried tomato,pesto and Mozzarella cheese</li>
        <li class="menu-item menu-item--stack">Mozzarella and salami<br>Cheese and ham<br>Cheese and onion<br>Cheese and tomato<br><span class="aside">(Paninis with fillings as above coming soon! One filling £4.20, Two filling £5.20)</span></li>
        <li class="menu-item"><span>Local butchers beef burger meal,served with chips and salad</span><span class="price">£7.95</span></li>
        <li class="menu-item"><span>Home made chicken fillet burger meal, served with chips and salad</span><span class="price">£7.95</span></li>
        <li class="menu-item"><span>Burger in a bun( on its own)</span><span class="price">£4.20</span></li>
        <li class="menu-item"><span>Pies assorted</span><span class="price">£2.50</span></li>
        <li class="menu-item"><span>Pie with beans</span><span class="price">£3.50</span></li>
        <li class="menu-item"><span>Pie with chips</span><span class="price">£5.00</span></li>
        <li class="menu-item"><span>Pie with beans and chips</span><span class="price">£6.00</span></li>
        <li class="menu-item"><span>Basket of chips</span><span class="price">£3.50</span></li>
        <li class="menu-item"><span>Chip butty</span><span class="price">£2.00</span></li>
        <li class="menu-item"><span>Chips &amp; beans</span><span class="price">£4.50</span></li>
        <li class="menu-item"><span>Chips &amp; cheese</span><span class="price">£4.50</span></li>
        <li class="menu-item"><span>Rolls with assorted cold fillings</span><span class="price">£2.20 - £3.20</span></li>
      </ul>
      <p class="note note--first">Gluten free bread and cakes available- ask staff!<br>At the hight of the season evening meals available.</p>
      <p class="note note--ask">Ask staff for more information.</p>
    </section>

    <div class="column-divider"></div>

    <section class="column column--drinks">
      <h2 class="section-heading">Refreshments</h2>
      <ul class="menu-list">
        <li class="menu-item"><span>Tea</span><span class="price">£1.50</span></li>
        <li class="menu-item"><span>Filter Coffee, decaf coffee, plain hot chocolate</span><span class="price">£2.00</span></li>
        <li class="menu-item"><span>Selection of herbal teas</span><span class="price">£2.00</span></li>
        <li class="menu-item"><span>Specialty strawberry, raspberry, apple &amp; mint tea( black tea with your choice of syrup)</span><span class="price">£2.50</span></li>
        <li class="menu-item"><span>Assorted premium “Leaf House” teas</span><span class="price">£2.50</span></li>
        <li class="menu-item"><span>Hot chocolate with cream</span><span class="price">£2.20</span></li>
        <li class="menu-item"><span>Hot chocolate with marsh mallows</span><span class="price">£2.20</span></li>
        <li class="menu-item"><span>Hot chocolate with cream &amp; marsh mallows</span><span class="price">£2.20</span></li>
        <li class="menu-item"><span>Hot chocolate with brandy</span><span class="price">£3.50</span></li>
        <li class="menu-item"><span>Hot chocolate with brandy,<br>marsh mallows &amp; cream</span><span class="price">£4.50</span></li>
        <li class="menu-item"><span>Cafe Latte/Cappucino</span><span class="price">£2.50</span></li>
        <li class="menu-item"><span>Squirrel Latte</span><span class="price">£3.50</span></li>
        <li class="menu-item"><span>Chocolate Latte</span><span class="price">£3.50</span></li>
        <li class="menu-item"><span>Cinnamon Latte</span><span class="price">£3.50</span></li>
        <li class="menu-item"><span>Caramel Latte</span><span class="price">£3.50</span></li>
        <li class="menu-item"><span>Butterscotch Latte</span><span class="price">£3.50</span></li>
        <li class="menu-item"><span>Gingerbread Latte</span><span class="price">£3.50</span></li>
        <li class="menu-item"><span>Mocha</span><span class="price">£3.50</span></li>
        <li class="menu-item"><span>Glass of milk</span><span class="price">£1.20</span></li>
        <li class="menu-item"><span>Milkshakes</span><span class="price">£2.00</span></li>
        <li class="menu-item"><span>Still or Sparkling water</span><span class="price">£1.80</span></li>
        <li class="menu-item"><span>Cans of juice</span><span class="price">£1.60</span></li>
        <li class="menu-item"><span>Cartons of juice</span><span class="price">£1.30</span></li>
      </ul>
      <p class="note note--first">We use semi skimmed milk only</p>
      <p class="note note--season">At the hight of the season evening meals available. Ask staff for more information.</p>
    </section>

    <div class="footer-rule"></div>
    <footer class="footer">
      <p>Elspeth’s @ Lochan Cafe, Lochside, Strathbeg, PH99 4QX. Tel:01234567890</p>
      <p>Like us on our page</p>
    </footer>
  </main>
</body>
</html>
```